Podcast Cover Art for Fast Growing Show (Ill include a gracious tip!)

This artwork is for "The Steadfast Fellow Show." The podcast is for men, and it's all about self-improvement, confidence, success, money, women and masculinity. It's for the guy who wants to improve himself. I'd like for my picture to be included — in black and white — and I want the text to read: "The Steadfast Fellow Show" and somewhere in there it'll say: "with Dale Prowen." I'm open to color schemes. The podcast is a little edgy so I'd like for that to be represented in the design. Thank you! (((Here's the podcast page if you wanna check it out: http://steadfastfellowshow.castorbit.net/)))

Target Market(s)

Men who want to attract women and improve their lives!

Font styles to use
Serif

Colors

Designer to choose colors to be used in the design.

Requirements
Must have
• My image in it (in black and white) and the two titles: "The Steadfast Fellow Show" and "with Dale Prowen"
Nice to have
• My logo in it somehow (which is the arrow looking logo attached below). I've also found that my image looks best in black and white and with a circular type cut out (although I'm open to different design ideas). I've attached my logo with a circular cut out below so you can see what I'm talking about.
Should not have
• Flowers. Teddy bears. ice cream.

```html
<!DOCTYPE html>
<html lang="en">
<head>
<meta charset="utf-8">
<title>The Steadfast Fellow Show — Cover Art</title>
<link rel="stylesheet" href="https://fonts.googleapis.com/css2?family=Oswald:wght@600&family=Roboto+Slab:wght@800&display=swap">
<style>
  :root {
    --page: #ffffff;
    --ink: #0b0b0b;
    --paper: #e2e2e2;
    --title: #f4f4f4;
    --photo-light: #bdbdbd;
    --photo-dark: #2a2a2a;
    --ring: #ffffff;
  }
  * { margin: 0; padding: 0; box-sizing: border-box; }
  html, body {
    width: 1200px; height: 1170px; overflow: hidden;
    background: var(--page);
  }
  .canvas { position: relative; width: 1200px; height: 1170px; }
  .cover {
    position: absolute; left: 194px; top: 172px;
    width: 813px; height: 813px; overflow: hidden;
    background: var(--paper);
  }
  .cover__backdrop { position: absolute; inset: 0; }
  .cover__title {
    position: absolute; left: 0; right: 0; top: 38px;
    text-align: center; color: var(--title);
    font-family: "Oswald", "Arial Narrow", sans-serif; font-weight: 600;
    text-transform: uppercase; line-height: 1;
  }
  .cover__title-main { display: block; font-size: 62px; letter-spacing: 2px; }
  .cover__title-sub { display: block; font-size: 44px; letter-spacing: 2px; margin-top: 14px; }
  .host-portrait {
    position: absolute; left: 205px; top: 188px;
    width: 402px; height: 402px; border-radius: 50%;
    border: 6px solid var(--ring);
    background: radial-gradient(circle at 50% 40%, var(--photo-light) 0%, #8a8a8a 45%, var(--photo-dark) 100%);
    box-shadow: 0 14px 26px rgba(0,0,0,0.35);
  }
  .brand-mark {
    position: absolute; left: 0; right: 0; top: 650px;
    display: flex; justify-content: center; align-items: center; gap: 10px;
    font-family: "Roboto Slab", Georgia, serif; font-weight: 800;
    font-size: 26px; letter-spacing: 2px; color: var(--ink);
  }
  .brand-mark__square { width: 18px; height: 18px; background: var(--ink); }
  .cover__host {
    position: absolute; left: 0; right: 0; top: 730px;
    text-align: center; color: var(--ink);
    font-family: "Roboto Slab", Georgia, serif; font-weight: 800;
    font-size: 44px; letter-spacing: 2px; text-transform: uppercase; line-height: 1;
  }
</style>
</head>
<body>
<main class="canvas">
  <section class="cover">
    <svg class="cover__backdrop" width="813" height="813" viewBox="0 0 813 813" aria-hidden="true">
      <rect width="813" height="813" fill="var(--paper)"/>
      <path fill="var(--ink)" d="M0 0 H813 V470 L800 466 L788 472 L772 463 L760 468 L744 459 L731 465 L716 462 L700 470 L686 464 L672 468 L655 460 L640 466 L620 470 L600 468 L210 470 L190 466 L176 472 L160 468 L148 474 L130 470 L118 462 L104 468 L90 466 L78 472 L62 464 L48 470 L34 468 L20 474 L8 470 L0 472 Z"/>
    </svg>
    <h1 class="cover__title">
      <span class="cover__title-main">The Steadfast Fellow</span>
      <span class="cover__title-sub">Show</span>
    </h1>
    <div class="host-portrait" role="img" aria-label="Black and white portrait of host Dale Prowen, hands steepled, in a circular cut-out"></div>
    <div class="brand-mark"><span class="brand-mark__square"></span><span>STEADFAST</span></div>
    <p class="cover__host">With Dale Prowen</p>
  </section>
</main>
</body>
</html>
```